Compass of Quiet Mornings book cover design

Book cover - the book contains 52 chapters - 2 for each letter of the alphabet, so a yearlong focus on Leadership. The Intent is to communicate that leadership is common sense. It just isn’t common practice. This book allows the reader to focus on one leadership word each week for a yearlong focus on improving one’s leadership. It is full of stories relating to the 52 words that will challenge and inspire the reader.
Target Market(s)
Leaders / Emerging Leaders
Industry/Entity Type
All
Requirements
Must have
- Appeal to executives
Nice to have
- Simplicity
Should not have
- Cartoon feel

```html
<!DOCTYPE html>
<html lang="en">
<head>
<meta charset="utf-8">
<title>Compass of Quiet Mornings — Book Cover</title>
<link rel="stylesheet" href="https://fonts.googleapis.com/css2?family=Bebas+Neue&family=Monoton&family=Titan+One&display=swap">
<style>
  :root {
    --forest: #214d31;
    --fern: #3b8253;
    --mint: #8cff8c;
    --paper: #ffffff;
    --crimson: #c0003a;
  }
  html, body {
    margin: 0;
    padding: 0;
    overflow: hidden;
    background: var(--paper);
  }
  .cover {
    position: relative;
    width: 872px;
    height: 1200px;
    overflow: hidden;
    background: var(--paper);
  }
  .bands {
    position: absolute;
    inset: 0;
  }
  .title-block {
    position: absolute;
    left: 0;
    top: 446px;
    width: 872px;
  }
  .title-main {
    margin: 0;
    text-align: center;
    font-family: "Monoton", cursive;
    font-weight: 400;
    font-size: 84px;
    line-height: 96px;
    color: var(--crimson);
    letter-spacing: 1px;
  }
  .title-sub {
    margin: 0;
    text-align: center;
    font-family: "Titan One", sans-serif;
    font-size: 36px;
    line-height: 48px;
    color: var(--fern);
  }
  .author {
    position: absolute;
    right: 158px;
    top: 598px;
    margin: 0;
    font-family: "Bebas Neue", sans-serif;
    font-size: 46px;
    line-height: 46px;
    color: var(--forest);
    letter-spacing: 0.5px;
  }
</style>
</head>
<body>
<main class="cover">
  <svg class="bands" width="872" height="1200" viewBox="0 0 872 1200" aria-hidden="true">
    <!-- vertical bands -->
    <rect class="band band-forest-left" x="0" y="0" width="126" height="1200" fill="var(--forest)"/>
    <rect class="band band-fern-top" x="259" y="0" width="124" height="442" fill="var(--fern)"/>
    <rect class="band band-fern-bottom" x="259" y="672" width="124" height="528" fill="var(--fern)"/>
    <rect class="band band-mint-top" x="477" y="0" width="124" height="442" fill="var(--mint)"/>
    <rect class="band band-mint-bottom" x="477" y="672" width="124" height="528" fill="var(--mint)"/>
    <rect class="band band-forest-right" x="727" y="0" width="145" height="1200" fill="var(--forest)"/>
  </svg>
  <svg class="bands curls" width="872" height="1200" viewBox="0 0 872 1200" role="img" aria-label="Curling spiral flourishes growing from the edges of the bands">
    <circle cx="127" cy="285" r="54" fill="var(--forest)"/>
    <circle cx="262" cy="285" r="54" fill="var(--fern)"/>
    <circle cx="478" cy="404" r="54" fill="var(--mint)"/>
    <circle cx="727" cy="238" r="56" fill="var(--forest)"/>
    <circle cx="383" cy="951" r="56" fill="var(--fern)"/>
    <circle cx="600" cy="729" r="56" fill="var(--mint)"/>
    <circle cx="727" cy="925" r="56" fill="var(--forest)"/>
  </svg>

  <header class="title-block">
    <h1 class="title-main">COMPASS</h1>
    <p class="title-sub">of quiet mornings</p>
  </header>
  <p class="author">MARTIN CALLOWAY</p>
</main>
</body>
</html>
```